Re-branding for Structural Engineering firm

We need new business cards as part of our current re-branding. We have a new logo (attached), so the card design should incorporate this color scheme. We are a structural engineering firm providing structural building design and seismic consulting services. The final design should communicate professionalism and stability, with a modern look and feel.

```html
<!DOCTYPE html>
<html lang="en">
<head>
<meta charset="UTF-8">
<title>RMV Structural Engineering – Business Card</title>
<link href="https://fonts.googleapis.com/css2?family=Lato:wght@400;700&display=swap" rel="stylesheet">
<style>
  :root {
    --stage: #111111;
    --brand-blue: #2f7cc6;
    --brand-blue-light: #4a8fd6;
    --brand-grey: #86878b;
    --ink-grey: #5a5b5f;
    --paper: #ffffff;
  }
  * { margin: 0; padding: 0; box-sizing: border-box; }
  html, body {
    width: 1200px; height: 1000px; overflow: hidden;
    background: var(--stage);
    font-family: "Lato", sans-serif;
  }
  .stage { position: relative; width: 1200px; height: 1000px; }
  .card {
    position: absolute; width: 520px; height: 300px;
    border-radius: 22px; overflow: hidden;
    box-shadow: 0 18px 40px rgba(0,0,0,0.6);
  }
  .card-front {
    left: 50px; top: 250px;
    background: linear-gradient(135deg, var(--brand-blue), var(--brand-blue-light));
    display: flex; align-items: center; justify-content: center; gap: 16px;
  }
  .card-back { left: 630px; top: 450px; background: var(--paper); }
  .card svg.bg { position: absolute; inset: 0; }

  .front-mark-square { width: 44px; height: 44px; background: var(--paper); flex: none; }
  .front-name {
    color: var(--paper); font-weight: 700; font-size: 26px;
    line-height: 1.15; letter-spacing: 1px;
  }

  .person { position: absolute; left: 38px; top: 34px; }
  .person-name { color: var(--brand-blue); font-weight: 700; font-size: 20px; }
  .person-title { color: var(--ink-grey); font-size: 12px; margin-top: 2px; }

  .web-panel {
    position: absolute; left: 305px; top: 78px; width: 200px; height: 100px;
    background: var(--brand-grey); color: var(--paper);
    display: flex; align-items: center; justify-content: center;
    font-size: 16px; letter-spacing: 1px;
  }

  .contact {
    position: absolute; left: 38px; top: 148px; color: var(--paper);
    font-size: 12px; line-height: 1.35;
  }
  .contact .lines { margin-left: 22px; }
  .contact .row { display: flex; align-items: center; gap: 8px; font-size: 14px; margin-top: 2px; }
  .contact .row svg { width: 13px; height: 13px; flex: none; }
  .contact .sep { opacity: 0.8; padding: 0 6px; }

  .firm-mark {
    position: absolute; left: 396px; top: 192px; width: 116px;
    display: flex; flex-direction: column; align-items: center;
  }
  .firm-mark .square { width: 60px; height: 60px; background: var(--brand-blue); }
  .firm-mark .firm-name {
    margin-top: 6px; color: var(--brand-blue); font-weight: 700;
    font-size: 11px; line-height: 1.15; text-align: center; letter-spacing: 0.5px;
  }
</style>
</head>
<body>
<main class="stage">

  <section class="card card-front" aria-label="Card front">
    <div class="front-mark-square" aria-hidden="true"></div>
    <div class="front-name">RMV STRUCTURAL<br>ENGINEERING</div>
  </section>

  <section class="card card-back" aria-label="Card back">
    <svg class="bg" width="520" height="300" viewBox="0 0 520 300" aria-hidden="true">
      <defs>
        <linearGradient id="bandBlue" x1="0" y1="0" x2="1" y2="0">
          <stop offset="0" stop-color="#4a8fd6"/>
          <stop offset="1" stop-color="#2f7cc6"/>
        </linearGradient>
      </defs>
      <rect x="0" y="136" width="392" height="140" fill="url(#bandBlue)"/>
    </svg>

    <div class="person">
      <div class="person-name">Dana Whitlow S.E.</div>
      <div class="person-title">Principal</div>
    </div>

    <div class="web-panel">WWW.RMVSE.COM</div>

    <div class="contact">
      <div class="lines">
        <div>RMV Structural Engineering</div>
        <div>4150 Harbor Ridge Dr., Ste 210</div>
        <div>Lakeview, CA 92000</div>
      </div>
      <div class="row">
        <svg viewBox="0 0 24 24" aria-hidden="true"><path fill="#fff" d="M6.6 10.8a15.1 15.1 0 0 0 6.6 6.6l2.2-2.2a1 1 0 0 1 1-.25 11.4 11.4 0 0 0 3.6.57 1 1 0 0 1 1 1V20a1 1 0 0 1-1 1A17 17 0 0 1 3 4a1 1 0 0 1 1-1h3.5a1 1 0 0 1 1 1c0 1.25.2 2.45.57 3.57a1 1 0 0 1-.25 1z"/></svg>
        <span>555.201.3340<span class="sep">|</span>555.418.7725</span>
      </div>
      <div class="row">
        <svg viewBox="0 0 24 24" aria-hidden="true"><path fill="#fff" d="M2 5h20v14H2z"/><path fill="none" stroke="#2f7cc6" stroke-width="2" d="M2 5l10 8 10-8"/></svg>
        <span>dana@rmvse.com</span>
      </div>
    </div>

    <div class="firm-mark">
      <div class="square" aria-hidden="true"></div>
      <div class="firm-name">RMV STRUCTURAL<br>ENGINEERING</div>
    </div>
  </section>

</main>
</body>
</html>
```